Catalogue for our Medical Products for Print

We need a wonderful catalogue design with details our products in German. Products and website see www.vortelsupply.example.

See file attached, 1 catalogue generated automatically has to be pimped and added by short description of products.

Thank you for your help. We need the products descriptions in the overview copied into the catalogue.

Target Market(s)

Doctors and hospitals, private people as well.

Font styles to use
Sans Serif

Requirements
Must have
• Nice overview of our products and categories.
Nice to have
• Our colors like website

```html
<!DOCTYPE html>
<html lang="de">
<head>
<meta charset="utf-8">
<title>Vortel Supply – Inhaltsverzeichnis &amp; Bestellformular</title>
<link rel="stylesheet" href="https://fonts.googleapis.com/css2?family=Oswald:wght@400;500&family=Montserrat:wght@400;600;700&display=swap">
<style>
  :root{
    --red:#d9131b;
    --grey-stripe:#5f6166;
    --ink:#151515;
    --muted:#333;
    --stage:#eeeeee;
    --page-right:#e6e6e6;
    --rule:#444;
  }
  *{box-sizing:border-box;margin:0;padding:0}
  html,body{width:1200px;height:800px;overflow:hidden;background:var(--stage)}
  .spread{position:absolute;left:40px;top:183px;width:1120px;height:433px;display:flex}
  .page{position:relative;height:100%;overflow:hidden}
  .page--contents{width:567px;background:linear-gradient(90deg,#fff 40%,#e9e9e9 100%)}
  .page--order{width:553px;background:linear-gradient(90deg,#f0f0f0,var(--page-right))}

  .side-band{position:absolute;left:0;top:0;width:128px;height:100%;background:var(--red)}
  .side-band__title{position:absolute;left:108px;top:158px;transform:translate(-50%,-50%) rotate(-90deg);
    font:700 28px "Montserrat",sans-serif;color:#fff;white-space:nowrap;letter-spacing:.2px}
  .stripes{position:absolute;left:0;top:0;width:567px;height:433px}

  .toc{position:absolute;font-family:"Oswald",sans-serif;color:var(--ink)}
  .toc h2{font-weight:400;font-size:23px;line-height:26px;text-transform:uppercase;margin-bottom:14px}
  .toc li{list-style:none;font-size:11px;line-height:12.5px;text-transform:uppercase;margin-bottom:13px}
  .toc--doctors{left:163px;top:46px}
  .toc--private{left:344px;top:85px}

  .photo{position:absolute;left:0;top:0;width:193px;height:100%;
    background:linear-gradient(160deg,#3cc7b4 0%,#6fb7e6 25%,#2f8fe0 55%,#7cc2ec 75%,#1e7fdc 100%)}
  .perforation{position:absolute;left:193px;top:0;height:100%;border-left:1.5px dotted #555}

  .form{position:absolute;left:193px;top:0;width:360px;height:100%;font-family:"Montserrat",sans-serif;color:var(--ink)}
  .portrait{position:absolute;left:40px;top:22px;width:61px;height:70px;background:linear-gradient(#d9d2cc,#f4f4f4);border-radius:4px}
  .contact-name{position:absolute;left:20px;top:97px;font-size:8.5px;font-weight:600}
  .brand{position:absolute;left:158px;top:54px;display:flex;align-items:center;gap:6px;
    font:700 18px "Montserrat",sans-serif;color:var(--red)}
  .brand__mark{width:16px;height:16px;background:var(--red)}
  .header-rule{position:absolute;left:20px;right:0;top:110px;border-top:2px solid var(--rule)}
  .label-red{position:absolute;left:20px;top:129px;font-size:8.5px;font-weight:700;color:var(--red)}
  .address{position:absolute;top:149px;font:400 8px/10px "Oswald",sans-serif;color:var(--ink)}
  .address--company{left:20px}
  .address--service{left:171px}
  .address a{color:var(--red);text-decoration:none}
  .field{position:absolute;left:20px;width:323px;display:flex;align-items:flex-end;font-size:8.5px;color:var(--muted)}
  .field span{white-space:nowrap}
  .field i{flex:1;border-bottom:1px solid var(--rule);margin-left:2px;height:8px}
  .blank{position:absolute;left:20px;width:323px;border-top:1px solid var(--rule)}
  .question{position:absolute;left:20px;top:286px;font-size:8.5px;color:var(--muted)}
  .consent{position:absolute;left:20px;top:367px;font-size:7px;line-height:9px;color:var(--muted)}
  .consent a{color:var(--red);text-decoration:none}
</style>
</head>
<body>
<div class="spread">
  <section class="page page--contents">
    <div class="side-band"></div>
    <svg class="stripes" viewBox="0 0 567 433" aria-hidden="true">
      <polygon points="0,300 128,433 100,433 0,330" fill="var(--grey-stripe)"/>
      <polygon points="0,345 88,433 62,433 0,372" fill="var(--grey-stripe)"/>
      <polygon points="0,388 45,433 20,433 0,413" fill="var(--grey-stripe)"/>
      <polygon points="128,300 236,433 128,433" fill="var(--red)"/>
      <polygon points="128,322 224,433 206,433 128,343" fill="#fff"/>
      <polygon points="128,358 194,433 176,433 128,379" fill="#fff"/>
      <polygon points="128,394 164,433 146,433 128,414" fill="#fff"/>
    </svg>
    <div class="side-band__title">Inhaltsverzeichnis</div>

    <div class="toc toc--doctors">
      <h2>Für Ärzte</h2>
      <ul>
        <li>Geräte &amp; Medizintechnik</li>
        <li>Beatmung &amp; Intubation</li>
        <li>Diagnostika</li>
        <li>Praxisgründung und Umbau</li>
        <li>Hygiene &amp; Desinfektion</li>
        <li>Notfall &amp; Erste-Hilfe</li>
        <li>Injektion &amp; Infusion</li>
        <li>Aktionen &amp; Angebote</li>
      </ul>
    </div>
    <div class="toc toc--private">
      <h2>Für Privatpersonen<br>und Firmen</h2>
      <ul>
        <li>Defibrillatoren</li>
        <li>Verbandskästen und Erste-Hilfe<br>Koffer</li>
        <li>Blutzuckermessgeräte</li>
        <li>Blutdruckmessgeräte</li>
        <li>Schilder</li>
        <li>Schutzausrüstung</li>
      </ul>
    </div>
  </section>

  <section class="page page--order">
    <div class="photo" role="img" aria-label="Foto: Stethoskop, Schutzbrille, Handschuhe, Mundschutz und blaue OP-Kleidung"></div>
    <div class="perforation"></div>
    <div class="form">
      <div class="portrait" role="img" aria-label="Porträtfoto der Ansprechpartnerin"></div>
      <div class="contact-name">Lena Hartmann, B.Sc.</div>
      <div class="brand"><span class="brand__mark"></span>VortelSupply</div>
      <div class="header-rule"></div>
      <div class="label-red">KONTAKT</div>
      <div class="address address--company">Vortel Supply GmbH<br>Lindenweg 12<br>4470 Bergstadt</div>
      <div class="address address--service"><a>www.vortelsupply.example</a><br>Kostenlose 24h Hotline: 0800 00 11 22<br>FAX: 0900 000 100 200</div>

      <div class="field" style="top:204px"><span>Name:</span><i></i></div>
      <div class="field" style="top:225px"><span>Anschrift:</span><i></i></div>
      <div class="field" style="top:245px"><span>Email fur Bestellbestatigung:</span><i></i></div>
      <div class="field" style="top:266px"><span>Telefon (optional) fur Ruckfragen:</span><i></i></div>
      <div class="question">Welche Produkte wollen Sie bestellen?</div>
      <div class="blank" style="top:315px"></div>
      <div class="blank" style="top:335px"></div>
      <div class="blank" style="top:356px"></div>
      <div class="consent">Ich akzeptiere die Datenschutzvereinbarung. Diese finden Sie online auf<br><a>www.vortelsupply.example</a></div>
    </div>
  </section>
</div>
</body>
</html>
```